Letterhead Design Project

I need a simple, clean and corporate letterhead & follow-on letterhead.
The follow-on letterhead should just have the logo only.
Final File Specs:
Full Bleed Size (starting document size)
213 x 300 mm
2517 x 3544 pixels
* Finished artwork should use the full bleed dimensions for best results.
Document Trim Size (final size after being cut)
210 x 297 mm
2480 x 3508 pixels
* Please be sure to keep all text within the safe margin.
Resolution 300 DPI
Accepted file types:-
Adobe Acrobat 9 Document (*.pdf) (recommended)
Adobe Illustrator CS3 Artwork (*.ai) (recommended)
Adobe Photoshop CS3 Image (*.psd) (recommended)
Bitmap Image (*.bmp)
GIF Image (*.gif)
JPEG Image (*.jpg,*.jpeg)
Microsoft PowerPoint 2010 Document (*.ppt)
Microsoft Publisher 2010 Document (*.pub)
Microsoft Word 2010 Document (*.doc)
PCX Image (*.pcx)
PICT Image (*.pic,*.pict,*.pct)
PNG Image (*.png)
PostScript Document (*.ps)
TIF Image (*.tif,*.tiff)
Windows Enhanced Metafile (*.emf)
Windows Metafile (*.wmf)
Requirements
Must have
- My letterhead must have:-
- Logo
- ACN - 482 617 309
- address - Suite 8, 51 Hartwell Ave, Marrowvale, NSW 2187
- phone - (02) 8371 5926
- fax - (02) 8352 6149
- email - info@brantorguard.com.au
- web - www.brantorguard.com.au
Follow-on letterhead should have the logo only

```html
<!DOCTYPE html>
<html lang="en">
<head>
<meta charset="utf-8">
<title>Brantor Guard – Letterhead &amp; Follow-on Letterhead</title>
<link href="https://fonts.googleapis.com/css2?family=Source+Sans+3:wght@400;600&display=swap" rel="stylesheet">
<style>
  :root {
    --backdrop: #2b2b2b;
    --paper: #ffffff;
    --navy: #1f1d45;
    --green: #9cc63b;
    --ink: #141414;
    --muted: #3a3866;
  }
  * { margin: 0; padding: 0; box-sizing: border-box; }
  html, body { width: 1200px; height: 1000px; overflow: hidden; }
  body {
    background: var(--backdrop);
    font-family: "Source Sans 3", "Myriad Pro", Arial, sans-serif;
    position: relative;
  }
  .sheet { position: absolute; background: var(--paper); }
  .sheet--first { left: 55px; top: 160px; width: 558px; height: 733px; }
  .sheet--follow { left: 614px; top: 157px; width: 521px; height: 735px; }

  .brand {
    position: absolute;
    display: flex;
    align-items: center;
    gap: 8px;
    color: var(--navy);
    font-weight: 600;
    font-size: 30px;
    white-space: nowrap;
  }
  .brand__mark { width: 22px; height: 22px; background: var(--green); }
  .sheet--first .brand { left: 178px; top: 30px; }
  .sheet--follow .brand { left: 178px; top: 30px; }

  .frame { position: absolute; border-radius: 28px; }
  .frame--outer { border: 2px solid var(--navy); }
  .frame--inner { border: 2px solid var(--green); border-radius: 24px; }
  .sheet--first .frame--outer { left: 27px; top: 97px; width: 458px; height: 631px; }
  .sheet--first .frame--inner { left: 41px; top: 108px; width: 429px; height: 548px; }
  .sheet--follow .frame--outer { left: 27px; top: 97px; width: 457px; height: 633px; }
  .sheet--follow .frame--inner { left: 40px; top: 113px; width: 431px; height: 599px; }

  .letter {
    position: absolute;
    width: 408px;
    color: var(--ink);
    font-size: 10.4px;
    line-height: 12.8px;
  }
  .sheet--first .letter { left: 54px; top: 170px; }
  .sheet--follow .letter { left: 53px; top: 169px; }
  .letter p.gap { margin-top: 12.8px; }
  .letter .salutation { margin-bottom: 12.8px; }
  .letter .signature { margin-top: 12.8px; padding-left: 2px; }

  .contact {
    position: absolute;
    left: 0; top: 0; width: 100%; height: 100%;
    color: var(--muted);
    font-size: 10.6px;
    line-height: 13.2px;
  }
  .contact__address { position: absolute; left: 64px; top: 655px; }
  .contact__label { color: var(--green); }
  .contact__lines { position: absolute; left: 165px; top: 668px; list-style: none; }
  .contact__lines li { display: flex; align-items: center; gap: 6px; }
  .contact__lines svg { width: 9px; height: 9px; fill: #888; }
  .contact__acn { position: absolute; left: 345px; top: 706px; }
</style>
</head>
<body>

<section class="sheet sheet--first" aria-label="Letterhead">
  <div class="brand"><span class="brand__mark"></span>Brantor Guard</div>
  <div class="frame frame--outer"></div>
  <div class="frame frame--inner"></div>

  <div class="letter">
    <p class="salutation">Dear Addressee Name:</p>
    <p>Andipsum dipsum nostis nulpute magnissis niatie te molor adignis sequips uscipisit, sit vel ipsuscing ent lut lan ulla feugait augueraesto odolore doluptatio cons dolor sismodo luptatuero do od dolore magnim dolor auguero eu facilis ea core estrud eugiat velis ad tat dio odolor augue magna corting eugait enim venibh et, quatumsan hendre tincinisi tisisl dolute moloreet atem velesequat alit aliquat, vel dolore faciduis dolore dignis dolorper il eugiamconsed deliquamcon henis alis atum duis at.</p>
    <p>Bore del ute faccum vercill aorper sent alit, venis autet, quipsustio eugue vero dolore velendre euis nos nonse dolessim illa feum dolor sumsan ectet lortincin vulputat amet, qui esto conulput acil in eugait vel essequam zzriusto diam, velit wissit autat.</p>
    <p>Obore dolor incip ea conummy nulput vel ullan henisim am in ute erciliqui ex ent et, quis augiat, commod tis enis num delit laor acing elis dolorer se eugue feu facinci liquis aut lut nulluptat er sum zzrit vulla consequis accum incidunt iusci blaortio odoloreet pratum veliquatie modit, quat. Ut nummodo exercilisl iriliqu ipsusto dolesequat. Ut wisl in ute consequam ad diam vulputpat lan hent vel doloreet utat ver si.</p>
    <p class="gap">Vullaorem iusci blamcon seniamcommy nit iureetum dolore con ea faccum iureet prat. In utat acidunt nullum venismolum ing exer iusci bla augue magna consequi tem veliquis nostion utpat.</p>
    <p>Nibh euipis esed ero doluptat. Ibh ex exeros exero dolesed dunt pratissi euis nismodipsum eu feuguerit ipisl incilla faccum am init praese tat velis augue corem iriliqu amconsequat. Magnim ipit in ea acincil esto et wisl esenim volenit lorem del ut aut la commy nibh eui tiniam iure mod tem vel ipisit, quis nonsequi blan exerosto odolorem il irit num vel dolore et irit aute te dolestrud tin hent utet ut praestrud ea faccum venim venim il er iustion sequipsum quat.</p>
    <p class="gap">Do ea acilisis dolore min ercing endre consequat. Ero consequis ad euguerat, siscidunt laor sum iuscipis nullaoreet, velent ilit amconul laorperit lore diatum dui bla facipit irit alis ad dolorpe rostrud tem essequat praesequam, coreet ip er sim dit, velisim inciliquam, quis adigna feugue dolore et irillaor.</p>
    <p>Adiam zzrit,</p>
    <p class="signature">Veliquatin Veraessi</p>
  </div>

  <div class="contact">
    <div class="contact__address">
      <div class="contact__label">Address:</div>
      <div>Suite 8,</div>
      <div>51 Hartwell Ave,</div>
      <div>Marrowvale,</div>
      <div>NSW 2187</div>
    </div>
    <ul class="contact__lines">
      <li><svg viewBox="0 0 10 10" aria-hidden="true"><path d="M2 1l2 2-1 1.2c.6 1.2 1.6 2.2 2.8 2.8L7 6l2 2-1.3 1.4C4.5 9 1 5.5.6 2.3z"/></svg>(02) 8371 5926</li>
      <li><svg viewBox="0 0 10 10" aria-hidden="true"><rect x="2.5" y="1" width="5" height="3"/><rect x="1" y="4" width="8" height="4" rx="1"/></svg>(02) 8352 6149</li>
      <li><svg viewBox="0 0 10 10" aria-hidden="true"><path d="M1 4l4-3 4 3v5H1z"/></svg>info@brantorguard.com.au</li>
      <li><svg viewBox="0 0 10 10" aria-hidden="true"><circle cx="5" cy="5" r="4.3"/></svg>www.brantorguard.com.au</li>
    </ul>
    <div class="contact__acn">ACN - 482 617 309</div>
  </div>
</section>

<section class="sheet sheet--follow" aria-label="Follow-on letterhead">
  <div class="brand"><span class="brand__mark"></span>Brantor Guard</div>
  <div class="frame frame--outer"></div>
  <div class="frame frame--inner"></div>

  <div class="letter">
    <p class="salutation">Dear Addressee Name:</p>
    <p>Andipsum dipsum nostis nulpute magnissis niatie te molor adignis sequips uscipisit, sit vel ipsuscing ent lut lan ulla feugait augueraesto odolore doluptatio cons dolor sismodo luptatuero do od dolore magnim dolor auguero eu facilis ea core estrud eugiat velis ad tat dio odolor augue magna corting eugait enim venibh et, quatumsan hendre tincinisi tisisl dolute moloreet atem velesequat alit aliquat, vel dolore faciduis dolore dignis dolorper il eugiamconsed deliquamcon henis alis atum duis at.</p>
    <p>Bore del ute faccum vercill aorper sent alit, venis autet, quipsustio eugue vero dolore velendre euis nos nonse dolessim illa feum dolor sumsan ectet lortincin vulputat amet, qui esto conulput acil in eugait vel essequam zzriusto diam, velit wissit autat.</p>
    <p>Obore dolor incip ea conummy nulput vel ullan henisim am in ute erciliqui ex ent et, quis augiat, commod tis enis num delit laor acing elis dolorer se eugue feu facinci liquis aut lut nulluptat er sum zzrit vulla consequis accum incidunt iusci blaortio odoloreet pratum veliquatie modit, quat. Ut nummodo exercilisl iriliqu ipsusto dolesequat. Ut wisl in ute consequam ad diam vulputpat lan hent vel doloreet utat ver si.</p>
    <p class="gap">Vullaorem iusci blamcon seniamcommy nit iureetum dolore con ea faccum iureet prat. In utat acidunt nullum venismolum ing exer iusci bla augue magna consequi tem veliquis nostion utpat.</p>
    <p>Nibh euipis esed ero doluptat. Ibh ex exeros exero dolesed dunt pratissi euis nismodipsum eu feuguerit ipisl incilla faccum am init praese tat velis augue corem iriliqu amconsequat. Magnim ipit in ea acincil esto et wisl esenim volenit lorem del ut aut la commy nibh eui tiniam iure mod tem vel ipisit, quis nonsequi blan exerosto odolorem il irit num vel dolore et irit aute te dolestrud tin hent utet ut praestrud ea faccum venim venim il er iustion sequipsum quat.</p>
    <p class="gap">Do ea acilisis dolore min ercing endre consequat. Ero consequis ad euguerat, siscidunt laor sum iuscipis nullaoreet, velent ilit amconul laorperit lore diatum dui bla facipit irit alis ad dolorpe rostrud tem essequat praesequam, coreet ip er sim dit, velisim inciliquam, quis adigna feugue dolore et irillaor.</p>
    <p>Adiam zzrit,</p>
    <p class="signature">Veliquatin Veraessi</p>
  </div>
</section>

</body>
</html>
```